Webdesign für Vernetzung christlicher Geschäftsleute
Zielgruppe
Die Vereinigung KRTWLE bezweckt die Vernetzung christlicher Geschäftsleute und die Verbreitung von Biblisch fundierten ethischen Geschäftsprinzipien. Die Zielgruppe umfasst Unternehmer und Verantwortungsträger aus Wirtschaft und Politik.
Aufgabenstellung
Ich suche einen Designer, welcher sich ernsthaft mit den Anforderungen und dem Design auseinandersetzt und eine Individuelle Lösung gestaltet.
Das Logo sowie ein unverbindlicher Vorschlag für die Strukturierung liegen bei.
Bitte keine 08/15 Business Stock Fotos (Händeschütteln, Meetings, Präsentationen).
Das Design soll folgende Seiten beinhalten (Beschreibung folgt):
- Startseite
- Standardseite (Titel, Text mit Bildern)
- Event-Detail Seite (Titel, Ort, Datum, ev. Foto, Beschreibungstext, ev. Map)
- Chapter Startseite
Die bestehende Webseite ist kein Massstab ;).

```html
<!DOCTYPE html>
<html lang="de">
<head>
<meta charset="utf-8">
<title>KRTWLE</title>
<link href="https://fonts.googleapis.com/css2?family=Open+Sans:wght@400;600;700&family=Cormorant+Garamond:wght@700&display=swap" rel="stylesheet">
<style>
:root{
  --red:#b0101e;
  --ink:#111;
  --text:#333;
  --footer:#dedede;
  --page:#f4f4f4;
  --white:#fff;
  --box:#eeeef0;
  --numeral:#8a8a8e;
}
*{margin:0;padding:0;box-sizing:border-box}
html,body{width:717px;height:1200px;overflow:hidden;background:var(--page);font-family:"Open Sans",sans-serif;color:var(--ink)}
.abs{position:absolute}
.screen{position:absolute;background:var(--white);box-shadow:0 6px 24px rgba(0,0,0,.12);overflow:hidden}
.desktop{left:26px;top:30px;width:508px;height:613px}
.mobile{left:552px;top:30px;width:140px;height:775px}
.brand{display:flex;align-items:center;gap:5px;font-weight:700;white-space:nowrap}
.brand-dot{border-radius:50%;border:1.5px solid var(--red);background:var(--white)}
.nav a{position:absolute;font-size:7px;font-weight:700;color:var(--ink);text-decoration:none}
.nav .active{border-bottom:1.5px solid var(--red);padding-bottom:1px}
.photo{position:absolute}
.photo-dove{background:radial-gradient(ellipse at 66% 50%,#f3f0ea 0 18%,transparent 32%),linear-gradient(180deg,#d9d9d9,#e6e6e6 60%,#c9c9c9 93%,#8c8c8c 100%)}
.photo-hall{background:linear-gradient(180deg,#e2e2e2 0 30%,#b9b9b9 30% 80%,#7a7a7a 80%)}
.photo-inn{background:linear-gradient(180deg,#cfcfcf 0 20%,#9b9b9b 20% 45%,#6f6f6f 45% 85%,#bdbdbd 85%)}
.chapter-tag{font-weight:700;display:flex;align-items:center;gap:3px}
.headline span{display:inline-block;background:var(--white);font-weight:700;padding-right:5px}
.section-title{position:absolute;color:var(--red);font-weight:600}
.copy{position:absolute;color:var(--text)}
.chapter-box{position:absolute;border:1.5px solid var(--red);background:var(--box);display:flex;align-items:center;justify-content:center;font-family:"Cormorant Garamond",serif;font-weight:700;color:var(--numeral)}
.chapter-label{position:absolute;font-weight:700}
.event-date{position:absolute;color:var(--red);font-weight:600}
.event-title{position:absolute;color:var(--text)}
.footer{position:absolute;left:0;right:0;bottom:0;background:var(--footer)}
</style>
</head>
<body>

<section class="screen desktop">
  <div class="brand abs" style="left:64px;top:20px;font-size:7px">
    <span class="brand-dot" style="width:20px;height:20px"></span>KRTWLE
  </div>
  <nav class="nav">
    <a class="active" style="left:264px;top:26px">START</a>
    <a style="left:315px;top:26px">ÜBER UNS</a>
    <a style="left:383px;top:26px">KONTAKT</a>
  </nav>

  <div class="photo photo-dove" role="img" aria-label="Weiße Taube auf einer Mauer vor grauem Himmel" style="left:128px;top:63px;width:299px;height:165px"></div>
  <div class="chapter-tag abs" style="left:373px;top:72px;font-size:7px">CHAPTER
    <svg width="9" height="8" viewBox="0 0 9 8"><rect y="0" width="9" height="1.5"/><rect y="3.2" width="9" height="1.5"/><rect y="6.4" width="9" height="1.5"/></svg>
  </div>
  <h1 class="headline abs" style="left:84px;top:102px;font-size:16px;line-height:22.5px">
    <span>SEIN</span><br><span>ZEICHEN</span><br><span>ÜBER UNS</span><br><span>IST LIEBE</span>
  </h1>

  <svg class="abs" style="left:92px;top:248px" width="160" height="15" viewBox="0 0 160 15">
    <g stroke-width="1.6">
      <path d="M7 0v15M0 7h14" stroke="#111"/>
      <path d="M43 0v15M36 7h14" stroke="#b0101e"/>
      <path d="M79 0v15M72 7h14" stroke="#111"/>
      <path d="M115 0v15M108 7h14" stroke="#b0101e"/>
      <path d="M151 0v15M144 7h14" stroke="#111"/>
    </g>
  </svg>

  <h2 class="section-title" style="left:79px;top:286px;font-size:7px">WILLKOMMEN</h2>
  <p class="copy" style="left:79px;top:303px;width:205px;font-size:5.1px;line-height:7.4px">Lorem ipsum dolor sit amet, consetetur sadipscing elitr, sed diam nonumy eirmod tempor invidunt ut labore et dolore magna aliquyam erat, sed diam voluptua. At vero eos et accusam et justo duo dolores et ea rebum. Stet clita kasd gubergren, no sea takimata sanctus est Lorem ipsum dolor sit amet. Lorem ipsum dolor sit amet, consetetur sadipscing elitr, sed diam nonumy eirmod tempor invidunt ut labore et dolore magna aliquyam erat, sed diam voluptua. At vero eos et accusam et justo duo dolores et ea rebum. Stet clita kasd gubergren, no sea takimata sanctus est Lorem ipsum dolor sit amet.</p>

  <h2 class="section-title" style="left:79px;top:387px;font-size:7px">CHAPTERS</h2>
  <div class="chapter-box" style="left:78px;top:404px;width:57px;height:37px;font-size:28px">I</div>
  <div class="chapter-box" style="left:151px;top:404px;width:57px;height:37px;font-size:28px">II</div>
  <div class="chapter-box" style="left:224px;top:404px;width:57px;height:37px;font-size:28px">III</div>
  <span class="chapter-label" style="left:79px;top:449px;font-size:6.5px">CHAPTER 1</span>
  <span class="chapter-label" style="left:153px;top:449px;font-size:6.5px">CHAPTER 2</span>
  <span class="chapter-label" style="left:228px;top:449px;font-size:6.5px">CHAPTER 3</span>

  <h2 class="section-title" style="left:333px;top:286px;font-size:7px">EVENTS</h2>
  <div class="photo photo-hall" role="img" aria-label="Modernes Veranstaltungsgebäude" style="left:333px;top:303px;width:94px;height:62px"></div>
  <span class="event-date" style="left:336px;top:371px;font-size:5px">22/03/2019</span>
  <span class="event-title" style="left:336px;top:380px;font-size:5px">LINDENHALLE | Seewilen</span>
  <svg class="abs" style="left:420px;top:381px" width="7" height="6" viewBox="0 0 7 6"><path d="M0 0l3 3-3 3M3.5 0l3 3-3 3" fill="none" stroke="#111" stroke-width="1.2"/></svg>
  <div class="photo photo-inn" role="img" aria-label="Gasthaus mit Sonnenschirmen auf der Terrasse" style="left:331px;top:398px;width:94px;height:62px"></div>
  <span class="event-date" style="left:334px;top:466px;font-size:5px">23/03/2019</span>
  <span class="event-title" style="left:334px;top:475px;font-size:5px">AUBERGE LA SOURCE | Monvallon</span>
  <svg class="abs" style="left:419px;top:476px" width="7" height="6" viewBox="0 0 7 6"><path d="M0 0l3 3-3 3M3.5 0l3 3-3 3" fill="none" stroke="#111" stroke-width="1.2"/></svg>

  <footer class="footer" style="height:112px">
    <strong class="abs" style="left:53px;top:28px;font-size:7.5px">KRTWLE</strong>
    <p class="abs" style="left:53px;top:41px;font-size:7.5px;line-height:11px;width:140px">Kreis Redlicher Tätiger<br>Wirtschaftsleute Europa</p>
    <p class="abs" style="left:228px;top:41px;font-size:7.5px;line-height:11px">info@krtwle.de<br>www.krtwle.org</p>
    <p class="abs" style="left:365px;top:41px;font-size:7.5px;line-height:11px">Datenschutz<br>Impressum</p>
  </footer>
</section>

<section class="screen mobile">
  <div class="brand abs" style="left:8px;top:7px;font-size:4.5px">
    <span class="brand-dot" style="width:9px;height:9px;border-width:1px"></span>KRTWLE
  </div>
  <svg class="abs" style="left:127px;top:8px" width="8" height="7" viewBox="0 0 8 7"><rect width="8" height="1.3"/><rect y="2.8" width="8" height="1.3"/><rect y="5.6" width="8" height="1.3"/></svg>

  <div class="photo photo-dove" role="img" aria-label="Weiße Taube auf einer Mauer vor grauem Himmel" style="left:0;top:45px;width:140px;height:79px"></div>
  <h1 class="headline abs" style="left:19px;top:28px;font-size:6.5px;line-height:9px">
    <span>SEIN ZEICHEN</span><br><span>ÜBER UNS IST</span><br><span>LIEBE</span>
  </h1>
  <div class="chapter-tag abs" style="left:111px;top:49px;font-size:3.5px">CHAPTER
    <svg width="4" height="4" viewBox="0 0 4 4"><path d="M0 0l2 1.6L4 0M0 2l2 1.6L4 2" fill="none" stroke="#b0101e" stroke-width=".8"/></svg>
  </div>

  <svg class="abs" style="left:11px;top:130px" width="80" height="8" viewBox="0 0 80 8">
    <g stroke-width="1">
      <path d="M4 0v8M0 4h8" stroke="#111"/>
      <path d="M21 0v8M17 4h8" stroke="#b0101e"/>
      <path d="M38 0v8M34 4h8" stroke="#111"/>
      <path d="M55 0v8M51 4h8" stroke="#b0101e"/>
      <path d="M72 0v8M68 4h8" stroke="#111"/>
    </g>
  </svg>

  <h2 class="section-title" style="left:12px;top:156px;font-size:6.5px">WILLKOMMEN</h2>
  <p class="copy" style="left:12px;top:168px;width:116px;font-size:3.6px;line-height:5.6px">Lorem ipsum dolor sit amet, consetetur sadipscing elitr, sed diam nonumy eirmod tempor invidunt ut labore et dolore magna aliquyam erat, sed diam voluptua. At vero eos et accusam et justo duo dolores et ea rebum. Stet clita kasd gubergren, no sea takimata sanctus est Lorem ipsum dolor sit amet. Lorem ipsum dolor sit amet, consetetur sadipscing elitr, sed diam nonumy eirmod tempor invidunt ut labore et dolore magna aliquyam erat, sed diam voluptua. At vero eos et accusam justo duo dolores et ea rebum.</p>

  <h2 class="section-title" style="left:12px;top:236px;font-size:6.5px">CHAPTERS</h2>
  <div class="chapter-box" style="left:12px;top:259px;width:51px;height:33px;font-size:24px">I</div>
  <div class="chapter-box" style="left:78px;top:259px;width:51px;height:33px;font-size:24px">II</div>
  <div class="chapter-box" style="left:12px;top:318px;width:51px;height:33px;font-size:24px">III</div>
  <span class="chapter-label" style="left:12px;top:299px;font-size:4.3px">CHAPTER 1</span>
  <span class="chapter-label" style="left:79px;top:299px;font-size:4.3px">CHAPTER 2</span>
  <span class="chapter-label" style="left:14px;top:358px;font-size:4.3px">CHAPTER 3</span>

  <h2 class="section-title" style="left:13px;top:383px;font-size:6.5px">EVENTS</h2>
  <div class="photo photo-hall" role="img" aria-label="Modernes Veranstaltungsgebäude" style="left:13px;top:403px;width:116px;height:77px"></div>
  <span class="event-date" style="left:16px;top:490px;font-size:4.2px">22/03/2019</span>
  <span class="event-title" style="left:16px;top:501px;font-size:4.2px">LINDENHALLE | Seewilen</span>
  <svg class="abs" style="left:121px;top:501px" width="8" height="7" viewBox="0 0 8 7"><path d="M0 0l3.5 3.5L0 7M4 0l3.5 3.5L4 7" fill="none" stroke="#b0101e" stroke-width="1.3"/></svg>
  <div class="photo photo-inn" role="img" aria-label="Gasthaus mit Sonnenschirmen auf der Terrasse" style="left:12px;top:521px;width:116px;height:77px"></div>
  <span class="event-date" style="left:15px;top:607px;font-size:4.2px">23/03/2019</span>
  <span class="event-title" style="left:15px;top:618px;font-size:4.2px">AUBERGE LA SOURCE | Monvallon</span>
  <svg class="abs" style="left:120px;top:618px" width="8" height="7" viewBox="0 0 8 7"><path d="M0 0l3.5 3.5L0 7M4 0l3.5 3.5L4 7" fill="none" stroke="#b0101e" stroke-width="1.3"/></svg>

  <footer class="footer" style="height:133px;text-align:center;color:var(--text)">
    <strong class="abs" style="left:0;right:0;top:25px;font-size:4.5px;color:var(--ink)">KRTWLE</strong>
    <p class="abs" style="left:0;right:0;top:40px;font-size:4.5px;line-height:6.6px">Kreis Redlicher<br>Tätiger Wirtschafts-<br>leute Europa</p>
    <p class="abs" style="left:0;right:0;top:74px;font-size:4.5px;line-height:6.6px">info@krtwle.de<br>www.krtwle.org</p>
    <p class="abs" style="left:0;right:0;top:101px;font-size:4.5px;line-height:6.6px">Datenschutz<br>Impressum</p>
  </footer>
</section>

</body>
</html>
```